Business Card Design Project

We need business cards for our new business, Veltrano Skyworks. We specialize in aerial videography and photography via drone. Currently we are mainly focusing on real estate videography but will branch into other markets and may even host training classes for flying drones.
Cards should include:
Name
Phone Number
Email Address
Web address
We will need to customize for more than one person and would like those fields to be editable
eps file logos are uploaded now, thanks!
Target Market(s)
Real Estate Agents, hotels, rental agencies and people who have recently purchase drones
Industry/Entity Type
Videography

```html
<!DOCTYPE html>
<html lang="en">
<head>
<meta charset="utf-8">
<title>Veltrano Skyworks — Business Cards</title>
<link rel="stylesheet" href="https://fonts.googleapis.com/css2?family=Exo+2:wght@400;600&display=swap">
<style>
  :root {
    --stage: #2b2b2b;
    --ink: #0d0d0d;
    --ink-soft: #1c1c1c;
    --orange: #f08a1c;
    --orange-light: #f7a93a;
    --paper: #efefef;
    --paper-shade: #cfcfcf;
    --grey-text: #8a8a8a;
    --brand-dark: #1a1a1a;
    --brand-light: #9a9a9a;
  }
  * { box-sizing: border-box; margin: 0; padding: 0; }
  html, body { width: 1200px; height: 992px; overflow: hidden; }
  body {
    background: var(--stage);
    font-family: "Exo 2", Arial, sans-serif;
    position: relative;
  }

  .card {
    position: absolute;
    width: 26em;
    height: 15em;
    overflow: hidden;
    box-shadow: 0 0.6em 1.6em rgba(0,0,0,0.55);
  }
  .card--large { font-size: 20px; }
  .card--small { font-size: 10px; }

  .card__art { position: absolute; inset: 0; width: 100%; height: 100%; }

  /* Front: contact side */
  .card-front { background: var(--ink); }
  .contact {
    position: absolute;
    left: 2.2em;
    top: 3.4em;
  }
  .contact__name {
    color: var(--orange);
    font-size: 1.35em;
    font-weight: 400;
    margin-bottom: 0.45em;
  }
  .contact__row {
    display: flex;
    align-items: center;
    gap: 0.55em;
    color: var(--grey-text);
    font-size: 0.72em;
    line-height: 1.75;
  }
  .contact__icon { width: 1.1em; height: 1.1em; flex: none; }

  .brand {
    position: absolute;
    display: flex;
    align-items: center;
    gap: 0.45em;
    font-weight: 600;
    white-space: nowrap;
  }
  .brand__mark { width: 1.1em; height: 1.1em; background: var(--orange); flex: none; }
  .brand--front { right: 1.8em; bottom: 2.6em; font-size: 0.8em; color: var(--brand-light); }

  /* Back: brand side */
  .card-back { background: radial-gradient(ellipse at 45% 40%, #ffffff 0%, var(--paper) 45%, var(--paper-shade) 100%); }
  .brand--back {
    left: 50%; top: 50%;
    transform: translate(-50%, -50%);
    font-size: 1.55em;
    color: var(--brand-dark);
  }

  /* Standalone brand lockup */
  .brand--lockup {
    left: 70px;
    top: 800px;
    font-size: 38px;
    color: var(--brand-light);
  }
</style>
</head>
<body>

  <!-- Large front card -->
  <section class="card card--large card-front" style="left:60px; top:110px;">
    <svg class="card__art" viewBox="0 0 520 300" preserveAspectRatio="none" aria-hidden="true">
      <defs>
        <linearGradient id="orangeBandA" x1="0" y1="0" x2="1" y2="1">
          <stop offset="0" stop-color="#f7a93a"/><stop offset="1" stop-color="#e87a12"/>
        </linearGradient>
      </defs>
      <path d="M150 0 H520 V120 C470 70 380 40 300 40 C230 40 190 20 150 0 Z" fill="url(#orangeBandA)"/>
      <path d="M0 190 C60 250 150 260 240 262 C300 264 340 280 370 300 H0 Z" fill="url(#orangeBandA)"/>
    </svg>
    <div class="contact">
      <p class="contact__name">Your Name</p>
      <p class="contact__row">
        <svg class="contact__icon" viewBox="0 0 16 16"><path fill="#f08a1c" d="M3 1h3l1.5 4-2 1.3a9 9 0 0 0 4.2 4.2L11 8.5l4 1.5v3a2 2 0 0 1-2 2A12 12 0 0 1 1 3a2 2 0 0 1 2-2z"/></svg>
        000-000-0000
      </p>
      <p class="contact__row">
        <svg class="contact__icon" viewBox="0 0 16 16"><rect x="1" y="3" width="14" height="10" fill="#f08a1c"/><path d="M1 3l7 6 7-6" fill="none" stroke="#0d0d0d" stroke-width="1.3"/></svg>
        emailaddress@
      </p>
      <p class="contact__row">
        <svg class="contact__icon" viewBox="0 0 16 16"><circle cx="8" cy="8" r="6.5" fill="none" stroke="#8a8a8a" stroke-width="1.3"/><path d="M1.5 8h13M8 1.5c-3 3.5-3 9.5 0 13M8 1.5c3 3.5 3 9.5 0 13" fill="none" stroke="#8a8a8a" stroke-width="1"/></svg>
        website
      </p>
    </div>
    <div class="brand brand--front"><span class="brand__mark"></span>Veltrano Skyworks</div>
  </section>

  <!-- Large back card -->
  <section class="card card--large card-back" style="left:620px; top:110px;">
    <svg class="card__art" viewBox="0 0 520 300" preserveAspectRatio="none" aria-hidden="true">
      <polygon points="0,0 110,0 0,150" fill="#f08a1c"/>
      <polygon points="0,0 100,0 0,136" fill="#0d0d0d"/>
      <polygon points="520,300 410,300 520,150" fill="#f08a1c"/>
      <polygon points="520,300 420,300 520,164" fill="#0d0d0d"/>
    </svg>
    <div class="brand brand--back"><span class="brand__mark"></span>Veltrano Skyworks</div>
  </section>

  <!-- Standalone brand lockup -->
  <div class="brand brand--lockup"><span class="brand__mark"></span>Veltrano Skyworks</div>

  <!-- Small back card -->
  <section class="card card--small card-back" style="left:600px; top:740px;">
    <svg class="card__art" viewBox="0 0 520 300" preserveAspectRatio="none" aria-hidden="true">
      <polygon points="0,0 110,0 0,150" fill="#f08a1c"/>
      <polygon points="0,0 100,0 0,136" fill="#0d0d0d"/>
      <polygon points="520,300 410,300 520,150" fill="#f08a1c"/>
      <polygon points="520,300 420,300 520,164" fill="#0d0d0d"/>
    </svg>
    <div class="brand brand--back"><span class="brand__mark"></span>Veltrano Skyworks</div>
  </section>

  <!-- Small front card -->
  <section class="card card--small card-front" style="left:880px; top:760px;">
    <svg class="card__art" viewBox="0 0 520 300" preserveAspectRatio="none" aria-hidden="true">
      <path d="M150 0 H520 V120 C470 70 380 40 300 40 C230 40 190 20 150 0 Z" fill="url(#orangeBandA)"/>
      <path d="M0 190 C60 250 150 260 240 262 C300 264 340 280 370 300 H0 Z" fill="url(#orangeBandA)"/>
    </svg>
    <div class="contact">
      <p class="contact__name">Your Name</p>
      <p class="contact__row">
        <svg class="contact__icon" viewBox="0 0 16 16"><path fill="#f08a1c" d="M3 1h3l1.5 4-2 1.3a9 9 0 0 0 4.2 4.2L11 8.5l4 1.5v3a2 2 0 0 1-2 2A12 12 0 0 1 1 3a2 2 0 0 1 2-2z"/></svg>
        000-000-0000
      </p>
      <p class="contact__row">
        <svg class="contact__icon" viewBox="0 0 16 16"><rect x="1" y="3" width="14" height="10" fill="#f08a1c"/><path d="M1 3l7 6 7-6" fill="none" stroke="#0d0d0d" stroke-width="1.3"/></svg>
        emailaddress@
      </p>
      <p class="contact__row">
        <svg class="contact__icon" viewBox="0 0 16 16"><circle cx="8" cy="8" r="6.5" fill="none" stroke="#8a8a8a" stroke-width="1.3"/><path d="M1.5 8h13M8 1.5c-3 3.5-3 9.5 0 13M8 1.5c3 3.5 3 9.5 0 13" fill="none" stroke="#8a8a8a" stroke-width="1"/></svg>
        website
      </p>
    </div>
    <div class="brand brand--front"><span class="brand__mark"></span>Veltrano Skyworks</div>
  </section>

</body>
</html>
```